Business Card Design - Carrington Hill Lodge

We are looking at a new design for our business cards that has a modern and professional look. We run a residential aged care facility focussing on the care of residents. The cards will be used for potential clients, consultants and business opportunities in this sector. Blue and white is our main colours and would to see these colours incorporated in the design.
Industry/Entity Type
Business
Contact Information for Business Card
Carrington Hill Lodge, Darren Pelham, dpelham@carringtonhilllodge.com.au, Finance Manager, 0491 736 208, BCom, 48 Yarrabee Way, Ridgemont Park, Qld 4127.

```html
<!DOCTYPE html>
<html lang="en">
<head>
<meta charset="utf-8">
<title>Carrington Hill Lodge – Business Card</title>
<link rel="stylesheet" href="https://fonts.googleapis.com/css2?family=Open+Sans:ital,wght@0,400;0,600;1,400&family=Oswald:wght@400&display=swap">
<style>
  :root {
    --brand-blue: #4f7b94;
    --card-white: #ffffff;
    --ink: #2f2f2f;
    --ink-soft: #555555;
    --rule: #c9bfb4;
    --backdrop: #e9e7e4;
  }
  * { box-sizing: border-box; margin: 0; padding: 0; }
  html, body {
    width: 1200px; height: 1000px; overflow: hidden;
    background: var(--backdrop);
    font-family: "Open Sans", Arial, sans-serif;
  }
  .canvas { position: relative; width: 1200px; height: 1000px; }
  .card {
    position: absolute; left: 236px; width: 728px; height: 415px;
    box-shadow: 0 3px 10px rgba(0,0,0,0.18);
  }
  .card--front { top: 72px; background: var(--brand-blue); }
  .card--back { top: 512px; background: var(--card-white); }

  .front-name {
    position: absolute; left: 0; right: 0; top: 180px;
    text-align: center; color: var(--card-white);
    font-size: 36px; font-weight: 600; letter-spacing: 0.5px;
  }
  .front-web {
    position: absolute; left: 0; right: 0; top: 354px;
    text-align: center; color: var(--card-white);
    font-style: italic; font-size: 15px;
  }

  .brand {
    position: absolute; left: 82px; top: 160px;
    display: flex; align-items: center; gap: 10px;
  }
  .brand-dot { width: 26px; height: 26px; border-radius: 50%; background: var(--brand-blue); flex: none; }
  .brand-name { color: var(--brand-blue); font-size: 20px; font-weight: 600; white-space: nowrap; }

  .divider {
    position: absolute; left: 364px; top: 120px; width: 1px; height: 174px;
    background: linear-gradient(to bottom, rgba(201,191,180,0), var(--rule) 20%, var(--rule) 80%, rgba(201,191,180,0));
  }

  .contact { position: absolute; left: 400px; top: 112px; color: var(--ink); }
  .contact-name {
    font-family: "Oswald", "Arial Narrow", sans-serif;
    color: var(--brand-blue); font-size: 21px; line-height: 26px; text-transform: uppercase;
  }
  .contact-role { font-size: 15px; line-height: 20px; color: var(--ink-soft); }
  .contact-rule { width: 76px; height: 1px; background: var(--rule); margin: 8px 0 13px; }
  .contact-address { font-size: 15px; line-height: 20px; margin-bottom: 12px; }
  .contact-list { list-style: none; font-size: 15px; line-height: 23px; }
  .contact-list li { display: flex; align-items: center; gap: 7px; }
  .contact-list svg { width: 13px; height: 13px; fill: var(--brand-blue); flex: none; }
</style>
</head>
<body>
<main class="canvas">
  <section class="card card--front" aria-label="Card front">
    <p class="front-name">Carrington Hill Lodge</p>
    <p class="front-web">www.carringtonhilllodge.com.au</p>
  </section>

  <section class="card card--back" aria-label="Card back">
    <div class="brand">
      <span class="brand-dot"></span>
      <span class="brand-name">Carrington Hill Lodge</span>
    </div>

    <div class="divider"></div>

    <div class="contact">
      <h1 class="contact-name">Darren Pelham</h1>
      <p class="contact-role">Finance Manager</p>
      <div class="contact-rule"></div>
      <p class="contact-address">48 Yarrabee Way,<br>Ridgemont Park, Qld 4127</p>
      <ul class="contact-list">
        <li>
          <svg viewBox="0 0 16 16" aria-hidden="true"><path d="M3.5 1l2.5 0 1.2 3.3-1.6 1.2c.8 1.8 2.2 3.2 4 4l1.2-1.6L14 9.1V12c0 .9-.7 1.6-1.6 1.5C6.8 13 2.9 9.1 2.4 3.6 2.3 2.3 2.6 1 3.5 1z"/></svg>
          0491 736 208
        </li>
        <li>
          <svg viewBox="0 0 16 16" aria-hidden="true"><path d="M1 3h14v10H1z M2 4l6 4.5L14 4z" fill-rule="evenodd"/></svg>
          dpelham@carringtonhilllodge.com.au
        </li>
        <li>
          <svg viewBox="0 0 16 16" aria-hidden="true"><circle cx="8" cy="8" r="6.3" fill="none" stroke="#4f7b94" stroke-width="1.3"/><ellipse cx="8" cy="8" rx="2.6" ry="6.3" fill="none" stroke="#4f7b94" stroke-width="1.1"/><path d="M2 8h12" stroke="#4f7b94" stroke-width="1.1"/></svg>
          www.carringtonhilllodge.com.au
        </li>
      </ul>
    </div>
  </section>
</main>
</body>
</html>
```